Use it Or lose it Flyer for Dental Office

Need to design a home mailer, 6x9, for a use it or lose it dental insurance campaign. Insurance benefits are not rolled over in January.  Including a new patient special for $179 for Xray, Exam, Regular Cleaning. New patients will get an tamu k tooth brush if they bring in Flyer. In back I would like to advertise for Fennoway.
Our dental office is www.wrenfolddentalga.com

```html
<!DOCTYPE html>
<html lang="en">
<head>
<meta charset="utf-8">
<title>Wrenfold Dental Mailer</title>
<link rel="stylesheet" href="https://fonts.googleapis.com/css2?family=Cinzel:wght@500;700&family=Poppins:wght@400;600&family=Montserrat:wght@500;700&family=Oswald:wght@700&family=Caveat:wght@500;700&display=swap">
<style>
  :root {
    --backdrop: #1a1a1a;
    --cream: #efede8;
    --cream-deep: #e6e3dd;
    --white: #ffffff;
    --forest: #46695a;
    --sage: #8aa8a0;
    --taupe: #8f807d;
    --swoop: #a9a3a0;
    --ink: #141414;
    --rule: #c9c5bf;
    --photo-a: #55705c;
    --photo-b: #2f5a49;
    --photo-c: #d8d2c8;
  }
  * { box-sizing: border-box; margin: 0; padding: 0; }
  html, body { width: 934px; height: 1200px; overflow: hidden; background: var(--backdrop); }
  .canvas { position: relative; width: 934px; height: 1200px; }

  .card { position: absolute; left: 98px; width: 744px; height: 495px; background: var(--cream); overflow: hidden; }
  .card--front { top: 88px; }
  .card--back { top: 617px; background: var(--white); }

  .hero { position: absolute; left: 0; top: 0; width: 744px; height: 300px; }

  .brand-glow {
    position: absolute; left: 10px; top: 20px; width: 180px; height: 140px;
    background: radial-gradient(ellipse at center, rgba(255,255,255,.95) 0%, rgba(255,255,255,.8) 35%, rgba(255,255,255,0) 72%);
  }
  .brand-name {
    position: absolute; left: 35px; top: 76px; width: 130px; text-align: center;
    font-family: "Cinzel", serif; font-weight: 500; color: var(--taupe);
    font-size: 19px; line-height: 1.1; letter-spacing: 1px;
  }
  .brand-name small { display: block; margin-top: 3px; font-size: 9px; letter-spacing: 4px; }

  .campaign {
    position: absolute; left: 36px; top: 272px;
    font-family: "Poppins", sans-serif; font-size: 13px; font-weight: 600; color: var(--forest);
    letter-spacing: .3px;
  }
  .campaign span { font-weight: 400; color: #3a3a3a; }

  .headline {
    position: absolute; left: 34px; top: 318px;
    font-family: "Cinzel", serif; font-weight: 700; color: var(--ink);
    font-size: 62px; line-height: 64px; letter-spacing: -1px;
  }

  .special {
    position: absolute; left: 503px; top: 300px; width: 142px; height: 142px; border-radius: 50%;
    background: var(--forest); color: var(--white); text-align: center;
    font-family: "Poppins", sans-serif;
  }
  .special__lead { position: absolute; top: 12px; width: 100%; font-size: 12px; font-weight: 600; line-height: 15px; }
  .special__price { position: absolute; top: 44px; width: 100%; font-family: "Oswald", sans-serif; font-size: 50px; font-weight: 700; line-height: 52px; letter-spacing: -1px; }
  .special__note { position: absolute; top: 103px; width: 100%; font-size: 9px; line-height: 11px; }

  .accent-dot { position: absolute; left: 657px; top: 305px; width: 62px; height: 62px; border-radius: 50%; background: var(--sage); }

  .footer-rule { position: absolute; left: 36px; right: 32px; top: 451px; border-top: 1px solid var(--rule); }
  .footer-offer {
    position: absolute; left: 36px; top: 465px;
    font-family: "Poppins", sans-serif; font-size: 11.5px; color: #2b2b2b;
  }
  .footer-offer strong { font-weight: 600; }
  .footer-mark { position: absolute; left: 454px; top: 465px; width: 18px; height: 18px; border-radius: 50%; background: var(--sage); }
  .footer-url {
    position: absolute; right: 32px; top: 466px;
    font-family: "Cinzel", serif; font-weight: 500; font-size: 13px; color: var(--ink);
  }

  .back-panel { position: absolute; left: 0; top: 0; width: 396px; height: 495px; background: var(--cream); }
  .back-brand { position: absolute; left: 0; top: 40px; width: 396px; text-align: center; font-family: "Cinzel", serif; font-weight: 500; color: var(--taupe); }
  .back-brand__mark { display: block; margin: 0 auto 12px; width: 44px; height: 44px; border-radius: 50%; background: var(--forest); }
  .back-brand__name { display: block; font-size: 34px; line-height: 1; letter-spacing: 2px; }
  .back-brand__sub { display: block; margin-top: 8px; font-family: "Montserrat", sans-serif; font-size: 13px; letter-spacing: 7px; color: #7a7270; }

  .aligner-photo { position: absolute; left: 90px; top: 178px; width: 220px; height: 215px; }
  .available {
    position: absolute; left: 276px; top: 222px; transform: rotate(12deg);
    font-family: "Caveat", cursive; font-weight: 500; font-size: 20px; line-height: 20px; color: var(--forest); text-align: left;
  }
  .available strong { display: block; font-weight: 500; font-size: 22px; }

  .hours {
    position: absolute; left: 62px; top: 403px; width: 282px; height: 34px;
    display: flex; align-items: center; background: var(--cream-deep);
    font-family: "Montserrat", sans-serif; font-weight: 500; font-size: 11.5px; line-height: 1.1; color: var(--forest); text-align: center;
  }
  .hours__slot { flex: 1; }
  .hours__slot + .hours__slot { border-left: 1px solid var(--taupe); }
  .phone {
    position: absolute; left: 0; width: 396px; top: 445px; text-align: center;
    font-family: "Montserrat", sans-serif; font-weight: 700; font-size: 23px; color: var(--forest);
  }
</style>
</head>
<body>
<main class="canvas">

  <section class="card card--front">
    <svg class="hero" viewBox="0 0 744 300" width="744" height="300">
      <defs>
        <linearGradient id="team-tones" x1="0" y1="0" x2="1" y2="1">
          <stop offset="0" stop-color="var(--photo-a)"/>
          <stop offset=".6" stop-color="var(--photo-b)"/>
          <stop offset="1" stop-color="var(--photo-c)"/>
        </linearGradient>
        <linearGradient id="patient-tones" x1="0" y1="0" x2="1" y2="1">
          <stop offset="0" stop-color="#2f2a28"/>
          <stop offset="1" stop-color="#cfc7bd"/>
        </linearGradient>
      </defs>
      <path d="M0 0 H744 V225 Q430 300 0 225 Z" fill="url(#team-tones)" role="img" aria-label="Photo of the dental team in green scrubs at the front desk"/>
      <path d="M0 225 Q430 300 744 225 V245 Q430 290 0 250 Z" fill="var(--swoop)"/>
      <g role="img" aria-label="Photo of a patient checking her smile in a hand mirror">
        <circle cx="487" cy="247" r="55" fill="url(#patient-tones)" stroke="var(--white)" stroke-width="3"/>
      </g>
      <g role="img" aria-label="Photo of a hygienist showing a smiling patient his teeth">
        <circle cx="639" cy="214" r="78" fill="url(#patient-tones)" stroke="var(--white)" stroke-width="3"/>
      </g>
    </svg>
    <div class="brand-glow"></div>
    <div class="brand-name">WRENFOLD<small>DENTAL</small></div>

    <p class="campaign">USE IT OR LOSE IT! <span>Insurance benefits don’t roll over in January.</span></p>
    <h1 class="headline">YOUR SMILE<br>IS WORTH IT...</h1>

    <div class="special">
      <p class="special__lead">A new<br>patient special</p>
      <p class="special__price">$179</p>
      <p class="special__note">for Xray, Exam,<br>Regular Cleaning</p>
    </div>
    <div class="accent-dot"></div>

    <div class="footer-rule"></div>
    <p class="footer-offer">New patients will get an <strong>TAMU K</strong> tooth brush if they bring in Flyer</p>
    <span class="footer-mark"></span>
    <p class="footer-url">WWW.WRENFOLDDENTALGA.COM</p>
  </section>

  <section class="card card--back">
    <div class="back-panel">
      <div class="back-brand">
        <span class="back-brand__mark"></span>
        <span class="back-brand__name">WRENFOLD</span>
        <span class="back-brand__sub">DENTAL</span>
      </div>

      <svg class="aligner-photo" viewBox="0 0 220 215" width="220" height="215" role="img" aria-label="Photo of a hand holding an open case with clear Fennoway aligners">
        <defs>
          <radialGradient id="aligner-tones" cx=".5" cy=".5" r=".6">
            <stop offset="0" stop-color="#d9d9d9"/>
            <stop offset=".6" stop-color="#8c8c8c"/>
            <stop offset="1" stop-color="#efede8"/>
          </radialGradient>
        </defs>
        <rect width="220" height="215" fill="url(#aligner-tones)"/>
      </svg>
      <p class="available"><strong>Fennoway</strong>Available</p>

      <div class="hours">
        <p class="hours__slot">Mon - Wed<br>9am - 5pm</p>
        <p class="hours__slot">Friday - Sunday<br>Closed</p>
        <p class="hours__slot">Thursday<br>8am - 4pm</p>
      </div>
      <p class="phone">(678) 555-0142</p>
    </div>
  </section>

</main>
</body>
</html>
```